K7 Services business card design contest. Use logo and create a professional layout.

See attached sample. Please sharpen all text and images, don't want any pix-elated content. We are looking for a clean look that quickly provides the information need. Please include our information provided on the sample card. Please feel free to offer any design changes. Please only user the colors provided: #2D3539 & #FFA500. Do not prefer any images other than the K7 Logo

Target Market(s)

Construction, Architects, General Contractors, residential

Industry/Entity Type

Business

Contact Information for Business Card

Company logo, Name, email, fax & phone

Font styles to use
Other font styles liked:
• Josefin Slab

Requirements
Must have
• Name
• Phone & Fax #'s
• address
• Logo
• Website url: www.kq7services.example
Nice to have
• Font Colors #2D3539 & #FFA400
• We prefer a white background.

```html
<!DOCTYPE html>
<html lang="en">
<head>
<meta charset="utf-8">
<title>K7 Services – Business Card</title>
<link href="https://fonts.googleapis.com/css2?family=Montserrat:wght@300;400;600&display=swap" rel="stylesheet">
<style>
  :root {
    --ink: #2D3539;
    --orange: #FFA500;
    --paper: #ffffff;
    --stage: #e4e4e4;
    --rule: #e2e2e2;
  }
  * { margin: 0; padding: 0; box-sizing: border-box; }
  html, body { width: 1200px; height: 852px; overflow: hidden; }
  body {
    background: var(--stage);
    font-family: "Montserrat", sans-serif;
    color: var(--ink);
    position: relative;
  }
  .card {
    position: absolute;
    top: 272px;
    width: 540px;
    height: 308px;
    background: var(--paper);
    border-radius: 14px;
    overflow: hidden;
    box-shadow: 0 6px 18px rgba(0,0,0,0.12);
  }
  .card--front { left: 40px; }
  .card--back { left: 620px; }

  .brand {
    display: flex;
    align-items: center;
    gap: 12px;
    font-weight: 600;
    color: var(--ink);
    letter-spacing: -0.5px;
    white-space: nowrap;
  }
  .brand__mark { background: var(--ink); flex: none; }
  .card--front .brand {
    position: absolute; left: 50%; top: 50%;
    transform: translate(-50%, -50%);
    font-size: 42px; gap: 14px;
  }
  .card--front .brand__mark { width: 30px; height: 30px; }

  .card--back .brand {
    position: absolute; left: 28px; top: 112px;
    font-size: 28px; gap: 9px;
  }
  .card--back .brand__mark { width: 20px; height: 20px; }

  .divider {
    position: absolute; left: 262px; top: 24px;
    width: 1px; height: 200px; background: var(--rule);
  }
  .contact {
    position: absolute; left: 282px; top: 32px; width: 240px;
  }
  .contact__name { color: var(--orange); font-weight: 300; font-size: 19px; line-height: 23px; }
  .contact__title { font-size: 11.5px; margin-top: 3px; }
  .contact__list { list-style: none; margin-top: 28px; font-size: 11.5px; line-height: 17px; }
  .contact__list li { display: flex; align-items: center; gap: 8px; }
  .contact__list svg { width: 11px; height: 11px; fill: var(--orange); flex: none; }
  .contact__address { margin-top: 4px; font-size: 11.5px; line-height: 17px; }
  .contact__services {
    margin-top: 12px; color: var(--orange); font-size: 12px; letter-spacing: 0.4px;
  }
  .swoosh { position: absolute; left: 0; bottom: 0; width: 540px; height: 308px; }
</style>
</head>
<body>

<section class="card card--front" aria-label="Card front">
  <div class="brand"><span class="brand__mark"></span>K7 Services</div>
</section>

<section class="card card--back" aria-label="Card back">
  <svg class="swoosh" viewBox="0 0 540 308" aria-hidden="true">
    <path d="M0 278 C200 292 400 302 540 306 L540 308 L0 308 Z" fill="var(--ink)"/>
    <path d="M110 308 C300 300 430 282 540 250 L540 308 Z" fill="var(--orange)"/>
  </svg>

  <div class="brand"><span class="brand__mark"></span>K7 Services</div>
  <div class="divider"></div>

  <div class="contact">
    <p class="contact__name">Marcus D. Hollis, MBA</p>
    <p class="contact__title">Director of Operations</p>
    <ul class="contact__list">
      <li>
        <svg viewBox="0 0 24 24"><path d="M6.6 10.8a15.1 15.1 0 0 0 6.6 6.6l2.2-2.2c.3-.3.7-.4 1-.2 1.1.4 2.3.6 3.6.6.6 0 1 .4 1 1V20c0 .6-.4 1-1 1A17 17 0 0 1 3 4c0-.6.4-1 1-1h3.5c.6 0 1 .4 1 1 0 1.3.2 2.5.6 3.6.1.3 0 .7-.2 1z"/></svg>
        (555) 014 - 2092
      </li>
      <li>
        <svg viewBox="0 0 24 24"><path d="M6 2h9l3 3v4H6zM3 10h18v9h-3v3H6v-3H3zm5 6v4h8v-4z"/></svg>
        (555) 018 - 4081
      </li>
      <li>
        <svg viewBox="0 0 24 24"><path d="M12 2a10 10 0 1 0 0 20 10 10 0 0 0 0-20zm6.9 6h-3a15 15 0 0 0-1.3-3.9A8 8 0 0 1 18.9 8zM12 4c.8 1.2 1.5 2.5 1.9 4h-3.8c.4-1.5 1.1-2.8 1.9-4zM4.3 14a8 8 0 0 1 0-4h3.4a16 16 0 0 0 0 4zm.8 2h3a15 15 0 0 0 1.3 3.9A8 8 0 0 1 5.1 16zm3-8h-3a8 8 0 0 1 4.3-3.9A15 15 0 0 0 8.1 8zM12 20c-.8-1.2-1.5-2.5-1.9-4h3.8c-.4 1.5-1.1 2.8-1.9 4zm2.3-6H9.7a14 14 0 0 1 0-4h4.6a14 14 0 0 1 0 4zm.3 5.9A15 15 0 0 0 15.9 16h3a8 8 0 0 1-4.3 3.9zm1.7-5.9a16 16 0 0 0 0-4h3.4a8 8 0 0 1 0 4z"/></svg>
        www.kq7services.example
      </li>
    </ul>
    <p class="contact__address">1720 Larkmoor Road, Suite<br>360-332 Fairview, Georgia, 30099</p>
    <p class="contact__services">DRONE | WEBCAM | VIDEO</p>
  </div>
</section>

</body>
</html>
```